Flyer for Medical practice welcoming new patients

We need a DL size brochure designed for Medical practice to advertise that we are accepting new patients. Our practice has special interests in women's and children's health and seniors health. Our existing advertising materials are in the colour scheme of purples I have uploaded our logo which includes our colour scheme.

Target Market(s)

Versatile to target anyone looking for a small medical practice that offers continuous care of seeing the same Doctor every time

Industry/Entity Type

Advertising

Font styles to use
Serif

Colors
6b449b
876aae
b7a5cc

Requirements
Must have
• The practice logo of just the picture not Dr Wanda Thorpe.
• Purple colour scheme.
• Practice name: Bramblecote Medical Practice.
• Address: 147 Tolley Rd, Bramblecote NSW 2500.
• Phone: 4371 5806.
• DL size brochure
• Welcoming new patients ( a strong emphasis needs to be placed on this)
• Nurse and onsite ECG's and lung function tests.
• Travel vaccines including yellow fever
• Bulk billing for tertiary students
• We would also like design to alter the text so that we can change the points to be reflect who we are targeting at the time.
Nice to have
• The practice logo with Dr Wanda Thorpe somewhere not as a feature as the practice no longer goes under this name but is still well known as Dr Thorpe's.

```html
<!DOCTYPE html>
<html lang="en">
<head>
<meta charset="utf-8">
<title>Bramblecote Medical Practice – Accepting New Patients</title>
<link href="https://fonts.googleapis.com/css2?family=Cabin:wght@400;500&family=Cabin+Condensed:wght@500&family=Roboto+Condensed:wght@700&display=swap" rel="stylesheet">
<style>
  :root {
    --purple-deep: #6b449b;
    --purple-mid: #876aae;
    --purple-soft: #b7a5cc;
    --lilac-pale: #e3d9ee;
    --grey-panel: #e8e8e8;
    --page-bg: #f2f2f2;
    --paper: #ffffff;
    --ink: #5a2e86;
  }
  * { margin: 0; padding: 0; box-sizing: border-box; }
  html, body {
    width: 1200px; height: 1000px; overflow: hidden;
    background: var(--page-bg);
  }
  .flyer {
    position: absolute; left: 380px; top: 36px;
    width: 440px; height: 928px;
    background: var(--paper);
    overflow: hidden;
    font-family: "Cabin", "Trebuchet MS", sans-serif;
    box-shadow: 0 4px 18px rgba(0,0,0,0.12);
  }
  .flyer__art { position: absolute; inset: 0; width: 440px; height: 928px; }
  .dot-field { position: absolute; border-radius: 50%; }
  .dot-field--top {
    left: 0; top: 150px; width: 300px; height: 180px;
    background: radial-gradient(ellipse at center, rgba(183,165,204,0.22), rgba(183,165,204,0) 70%);
  }
  .dot-field--bottom {
    left: 260px; top: 600px; width: 220px; height: 340px;
    background: radial-gradient(ellipse at center, rgba(183,165,204,0.24), rgba(183,165,204,0) 70%);
  }
  .brand {
    position: absolute; left: 8px; top: 178px;
    color: var(--ink);
    font-weight: 400; font-size: 28px; line-height: 32px;
  }
  .brand__mark {
    position: absolute; left: 18px; top: 42px;
    width: 120px; height: 120px; border-radius: 50%;
    border: 3px solid var(--lilac-pale);
  }
  .burst-text {
    position: absolute; left: 160px; top: 300px; width: 280px;
    text-align: center; color: #fff;
    font-family: "Cabin Condensed", "Arial Narrow", sans-serif;
    font-weight: 500; font-size: 38px; line-height: 56px;
    text-shadow: 2px 2px 2px rgba(40,15,70,0.75);
    letter-spacing: 0.5px;
  }
  .services {
    position: absolute; left: 8px; top: 536px;
    list-style: none; color: var(--ink);
    font-size: 18px; line-height: 25px;
    white-space: nowrap;
  }
  .services li { position: relative; padding-left: 22px; margin-bottom: 17px; }
  .services li::before {
    content: ""; position: absolute; left: 0; top: 8px;
    width: 11px; height: 11px; border-radius: 50%; background: var(--purple-deep);
  }
  .contact {
    position: absolute; right: 10px; top: 820px;
    text-align right; text-align: right; color: var(--ink);
    font-size: 15px; line-height: 20px; font-style: normal;
    white-space: nowrap;
  }
  .contact__title {
    font-family: "Roboto Condensed", "Arial Narrow", sans-serif;
    font-weight: 700; font-size: 15px; margin-bottom: 6px;
  }
  .contact__icon { display: inline-block; vertical-align: -2px; margin-right: 5px; }
  .contact__phone { margin-top: 4px; }
</style>
</head>
<body>
<main class="flyer">
  <svg class="flyer__art" viewBox="0 0 440 928" aria-hidden="true">
    <defs>
      <linearGradient id="burstFill" x1="0" y1="0" x2="0" y2="1">
        <stop offset="0" stop-color="#c3b3d8"/>
        <stop offset="0.5" stop-color="#9f86c2"/>
        <stop offset="0.52" stop-color="#8b6db4"/>
        <stop offset="1" stop-color="#6b449b"/>
      </linearGradient>
    </defs>
    <path d="M218,0 L440,0 L440,160 C440,200 420,216 380,216 C300,216 222,130 218,0 Z" fill="var(--grey-panel)"/>
    <path d="M120,0 L190,0 C200,150 300,232 440,240 L440,300 C270,290 140,170 120,0 Z" fill="var(--purple-mid)"/>
    <path d="M0,372 C130,340 270,318 390,312 C370,520 270,780 140,928 L0,928 Z" fill="var(--grey-panel)"/>
    <path d="M420,300 L440,292 L440,570 C360,760 270,850 225,928 L165,928 C300,760 400,520 420,300 Z" fill="var(--purple-deep)"/>
    <path d="M0,312 C100,284 200,268 310,262 L310,300 C200,308 100,322 0,348 Z" fill="var(--purple-mid)"/>
    <g transform="translate(300 374)">
      <polygon fill="url(#burstFill)" stroke="#fff" stroke-width="5" stroke-linejoin="round"
        points="140,0 121,15.9 135.2,36.2 112.7,46.7 121.2,70 96.8,74.3 99,99 74.3,96.8 70,121.2 46.7,112.7 36.2,135.2 15.9,121 0,140 -15.9,121 -36.2,135.2 -46.7,112.7 -70,121.2 -74.3,96.8 -99,99 -96.8,74.3 -121.2,70 -112.7,46.7 -135.2,36.2 -121,15.9 -140,0 -121,-15.9 -135.2,-36.2 -112.7,-46.7 -121.2,-70 -96.8,-74.3 -99,-99 -74.3,-96.8 -70,-121.2 -46.7,-112.7 -36.2,-135.2 -15.9,-121 0,-140 15.9,-121 36.2,-135.2 46.7,-112.7 70,-121.2 74.3,-96.8 99,-99 96.8,-74.3 121.2,-70 112.7,-46.7 135.2,-36.2 121,-15.9"/>
    </g>
  </svg>

  <div class="dot-field dot-field--top" role="img" aria-label="Faint lilac bubble pattern"></div>
  <div class="dot-field dot-field--bottom" role="img" aria-label="Faint lilac bubble pattern"></div>

  <span class="brand__mark"></span>
  <h1 class="brand">Bramblecote<br>Medical Practice</h1>

  <p class="burst-text">ACCEPTING<br>NEW<br>PATIENT!</p>

  <ul class="services">
    <li>Nurse on site for ECG's, lung function<br>tests, health assessments<br>and much more</li>
    <li>We offer travel vaccines<br>including yellow fever</li>
    <li>Bulk billing for tertiary<br>students</li>
  </ul>

  <address class="contact">
    <p class="contact__title">Contact Details:</p>
    <p><svg class="contact__icon" width="16" height="14" viewBox="0 0 16 14" aria-hidden="true"><path d="M1,7 L8,1 L15,7 M3,6 V13 H13 V6 M7,13 V9 H9 V13" fill="none" stroke="var(--purple-soft)" stroke-width="1.3"/></svg>147 Tolley Rd,</p>
    <p>Bramblecote NSW 2500.</p>
    <p class="contact__phone"><svg class="contact__icon" width="14" height="14" viewBox="0 0 14 14" aria-hidden="true"><rect width="14" height="14" rx="2" fill="var(--purple-soft)"/><path d="M5,3 C3,5 5,10 9,11 L10,9 L8.5,8 L7.5,9 C6.5,8.5 5.5,7 5.5,6 L6.5,5.2 L5.8,3.5 Z" fill="#fff"/></svg>4371 5806</p>
  </address>
</main>
</body>
</html>
```